Business Card Design

An energy company designed around renewable energy and energy storage that focuses on providing its energy at points on the grid that reduce costs and add value to the system.

Industry/Entity Type

Business

Contact Information for Business Card

Martin Delacroix
Executive Vice President
41 K ST NE
Washington, DC 20017
240-555-0183
mdelacroix@harborvoltco.example

```html
<!DOCTYPE html>
<html lang="en">
<head>
<meta charset="utf-8">
<title>Martin Delacroix — Business Card</title>
<link rel="stylesheet" href="https://fonts.googleapis.com/css2?family=Open+Sans:wght@400;600;700&display=swap">
<style>
  :root {
    --backdrop: #d9d9d7;
    --card: #0b0b0c;
    --card-edge: #161617;
    --pill: #1e1e1f;
    --accent: #f7941d;
    --text: #ffffff;
    --rule: #2a2a2b;
    --divider: #555556;
  }
  * { box-sizing: border-box; margin: 0; padding: 0; }
  html, body {
    width: 1200px; height: 900px; overflow: hidden;
    background: var(--backdrop);
    font-family: "Open Sans", Arial, sans-serif;
  }
  .sheet { position: relative; width: 1200px; height: 900px; }

  .card {
    position: absolute; left: 250px; width: 700px; height: 400px;
    background: linear-gradient(135deg, var(--card-edge), var(--card) 60%);
    overflow: hidden;
    box-shadow: 0 10px 24px rgba(0,0,0,.25);
  }
  .card--front { top: 40px; }
  .card--back { top: 460px; }

  .brand { position: absolute; display: flex; align-items: center; gap: 16px; }
  .card--front .brand { left: 50%; top: 50%; transform: translate(-50%, -50%); }
  .card--back .brand { left: 360px; top: 118px; }
  .brand__mark { width: 44px; height: 44px; background: var(--accent); }
  .brand__divider { width: 1px; height: 56px; background: var(--divider); }
  .brand__name {
    color: var(--text); font-weight: 700; font-size: 19px;
    letter-spacing: 2px; line-height: 1.1; text-transform: uppercase;
  }

  .person {
    position: absolute; left: 0; top: 120px;
    background: var(--pill); padding: 10px 24px 10px 40px;
    border-radius: 0 28px 28px 0;
  }
  .person__name { color: var(--text); font-size: 24px; font-weight: 400; line-height: 1.2; }
  .person__title { color: var(--accent); font-size: 15px; line-height: 1.3; }

  .card__rule {
    position: absolute; left: 0; right: 0; top: 214px; height: 1px; background: var(--rule);
  }

  .contact {
    position: absolute; right: 40px; bottom: 34px; list-style: none;
    color: var(--text); font-size: 17px; text-align: right; line-height: 1.5;
  }
  .contact li { display: flex; align-items: center; justify-content: flex-end; gap: 12px; }
  .contact svg { width: 14px; height: 14px; flex: none; fill: none; stroke: var(--accent); stroke-width: 1.6; }
</style>
</head>
<body>
<main class="sheet">

  <section class="card card--front" aria-label="Card front">
    <div class="brand">
      <span class="brand__mark"></span>
      <span class="brand__divider"></span>
      <span class="brand__name">Martin<br>Delacroix</span>
    </div>
  </section>

  <section class="card card--back" aria-label="Card back">
    <div class="person">
      <p class="person__name">Martin Delacroix</p>
      <p class="person__title">Executive Vice President</p>
    </div>
    <div class="brand">
      <span class="brand__mark"></span>
      <span class="brand__divider"></span>
      <span class="brand__name">Martin<br>Delacroix</span>
    </div>
    <div class="card__rule"></div>
    <ul class="contact">
      <li>240-555-0183
        <svg viewBox="0 0 14 14"><rect x="4" y="1" width="6" height="12" rx="1"/><line x1="6" y1="11" x2="8" y2="11"/></svg>
      </li>
      <li>41 K ST NE, Washington, DC 20017
        <svg viewBox="0 0 14 14"><path d="M7 13s-4-4.5-4-7.5a4 4 0 0 1 8 0C11 8.5 7 13 7 13z"/><circle cx="7" cy="5.5" r="1.5"/></svg>
      </li>
      <li>mdelacroix@harborvoltco.example
        <svg viewBox="0 0 14 14"><rect x="1" y="3" width="12" height="8"/><polyline points="1,3 7,8 13,3"/></svg>
      </li>
      <li>harborvoltco.example
        <svg viewBox="0 0 14 14"><rect x="1" y="6" width="7" height="4" rx="2" transform="rotate(-45 4.5 8)"/><rect x="6" y="4" width="7" height="4" rx="2" transform="rotate(-45 9.5 6)"/></svg>
      </li>
    </ul>
  </section>

</main>
</body>
</html>
```